Business Card Design for Photographer

Updating business card design. Must use included logo. We're a luxury wedding photography business. Elegancy, luxury, consistency are messages we wish to convey.

Visit our website at www.colvanderose.com to familiarize yourself more with our brand design currently (fonts, colors etc.). This is what we want to maintain.

Target Market(s)

Luxury Brides and Grooms

Industry/Entity Type

Wedding

Contact Information for Business Card

Current logo (attached to brief)
Name: Colin Vanderose
Phone: 5871302948
website/blog
Email

Requirements
Must have
• Current logo (attached to brief)
• Name: Colin Vanderose
• Phone: 5871302948
• website/blog
• Email
• Instagram username
Should not have
• bright colors, fonts that don't suit our brand (visit www.colvanderose.com)

```html
<!DOCTYPE html>
<html lang="en">
<head>
<meta charset="utf-8">
<title>Colin Vanderose Photographers – Business Card</title>
<link href="https://fonts.googleapis.com/css2?family=Crimson+Text&family=Tenor+Sans&display=swap" rel="stylesheet">
<style>
  :root {
    --backdrop: #e8e6e3;
    --card: #ffffff;
    --ink: #6b6b6b;
    --ink-dark: #5e5e5e;
    --band: #6e6e6e;
  }
  * { box-sizing: border-box; margin: 0; padding: 0; }
  html, body { width: 1200px; height: 1000px; overflow: hidden; }
  body { background: var(--backdrop); position: relative; font-family: "Crimson Text", Georgia, serif; color: var(--ink); }

  .card { position: absolute; left: 265px; width: 666px; height: 397px; background: var(--card); box-shadow: 0 4px 14px rgba(0,0,0,0.12); overflow: hidden; }
  .card-front { top: 73px; }
  .card-back { top: 532px; }

  .brand { position: absolute; text-align: center; font-family: "Tenor Sans", "Helvetica Neue", sans-serif; color: var(--ink); }
  .brand-mark { display: block; margin: 0 auto; background: var(--ink); }
  .brand-name, .brand-trade { display: block; white-space: nowrap; text-transform: uppercase; }

  .card-front .brand { left: 30px; top: 125px; width: 326px; }
  .card-front .brand-mark { width: 56px; height: 56px; }
  .card-front .brand-name { font-size: 26px; letter-spacing: 3px; margin-top: 22px; line-height: 30px; }
  .card-front .brand-trade { font-size: 13px; letter-spacing: 5px; margin-top: 6px; }

  .divider { position: absolute; left: 389px; top: 125px; width: 1.5px; height: 136px; background: var(--ink); }

  .contact { position: absolute; left: 422px; top: 118px; }
  .contact-name { font-size: 22px; color: var(--ink-dark); line-height: 30px; }
  .contact-list { list-style: none; margin-top: 18px; font-size: 16.5px; color: var(--ink-dark); }
  .contact-list li { display: flex; align-items: center; height: 21px; }
  .contact-list li.social { margin-top: 6px; }
  .contact-list svg { width: 12px; height: 12px; margin-right: 7px; fill: var(--ink-dark); flex: none; }

  .band { position: absolute; left: 0; bottom: 0; width: 100%; height: 32px; background: var(--band); }

  .card-back .brand { left: 0; top: 97px; width: 100%; }
  .card-back .brand-mark { width: 72px; height: 72px; }
  .card-back .brand-name { font-size: 33px; letter-spacing: 4px; margin-top: 30px; line-height: 40px; }
  .card-back .brand-trade { font-size: 17px; letter-spacing: 6px; margin-top: 10px; }

  .card-back .web { position: absolute; left: 0; bottom: 28px; width: 100%; text-align: center; font-size: 16.5px; letter-spacing: 1.2px; color: var(--ink-dark); }
</style>
</head>
<body>

<section class="card card-front">
  <div class="brand">
    <span class="brand-mark"></span>
    <span class="brand-name">Colin Vanderose</span>
    <span class="brand-trade">Photographers</span>
  </div>
  <div class="divider"></div>
  <div class="contact">
    <p class="contact-name">Colin Vanderose</p>
    <ul class="contact-list">
      <li><svg viewBox="0 0 12 12"><path d="M3 1 L5 3.5 L4 4.8 Q5.2 7 7.2 8 L8.5 7 L11 9 L9.8 11 Q5 10.5 1 3.2 Z"/></svg>5871302948</li>
      <li><svg viewBox="0 0 12 12"><path d="M1 2.5 H11 V9.5 H1 Z M1.8 3.2 L6 6.5 L10.2 3.2" /><path d="M1 2.5 L6 6.4 L11 2.5 V3.6 L6 7.5 L1 3.6 Z" fill="#fff"/></svg>colin@colvanderose.com</li>
      <li><svg viewBox="0 0 12 12"><circle cx="6" cy="6" r="5" fill="none" stroke="#5e5e5e" stroke-width="1.1"/><ellipse cx="6" cy="6" rx="2.2" ry="5" fill="none" stroke="#5e5e5e" stroke-width="1"/><path d="M1 6 H11" stroke="#5e5e5e" stroke-width="1"/></svg>www.colvanderose.com</li>
      <li class="social"><svg viewBox="0 0 12 12"><rect x="1.5" y="1.5" width="9" height="9" fill="none" stroke="#5e5e5e" stroke-width="1.4"/></svg>colvanderosephoto</li>
    </ul>
  </div>
  <div class="band"></div>
</section>

<section class="card card-back">
  <div class="brand">
    <span class="brand-mark"></span>
    <span class="brand-name">Colin Vanderose</span>
    <span class="brand-trade">Photographers</span>
  </div>
  <p class="web">www.colvanderose.com</p>
</section>

</body>
</html>
```